Korvesh Menu

Hi there,
My restaurant called "Korvesh" means Spice in hebrew.
We are middle eastern restaurant that specialist in dips,salads and hot bread baked on the spot and charcoal grilled meat skewers
The restaurant is pretty casual and the atmosphere is nice and customers feels like home.
on www.korvesh.com.au you can see photos of the restaurant and the food.
ill add up the menus that i would like to be design please and the logo that is on the front of the shop is been add up
thank you

Target Market(s)

The regulars of the restaurant is jewish/israelis

Industry/Entity Type

Restaurant

```html
<!DOCTYPE html>
<html lang="en">
<head>
<meta charset="utf-8">
<title>Korvesh Menu</title>
<link href="https://fonts.googleapis.com/css2?family=Crimson+Pro:ital,wght@0,400;0,700;1,700&family=Caveat:wght@500&family=Kalam:wght@400;700&family=Oswald:wght@500&family=Fjalla+One&display=swap" rel="stylesheet">
<style>
  :root {
    --canvas: #ffffff;
    --board: #111111;
    --board-light: #262626;
    --chalk: #f4f4f4;
    --gold: #f2b31e;
    --dash: #9a9a9a;
    --label: #444444;
    --icon-blue: #2f7fd6;
    --fb-blue: #3b5998;
  }
  * { margin: 0; padding: 0; box-sizing: border-box; }
  html, body { width: 1200px; height: 1000px; overflow: hidden; background: var(--canvas); }
  .sheet { position: relative; width: 1200px; height: 1000px; }

  .page {
    position: absolute; top: 73px; width: 561px; height: 793px; overflow: hidden;
    background: radial-gradient(ellipse at 45% 30%, var(--board-light) 0%, var(--board) 70%);
    color: var(--chalk);
  }
  .page--entree { left: 34px; }
  .page--mains { left: 613px; }
  .page--mains::after {
    content: ""; position: absolute; left: 0; right: 0; bottom: 0; height: 300px;
    background: radial-gradient(ellipse at 30% 85%, rgba(150,70,20,.35) 0%, rgba(80,30,10,.15) 40%, transparent 70%);
    pointer-events: none;
  }
  .page > * { position: absolute; z-index: 1; }

  .brand-name { top: 12px; font-family: "Crimson Pro", serif; font-size: 80px; font-weight: 400; line-height: 1; letter-spacing: 1px; }
  .brand-band {
    top: 105px; width: 248px; height: 87px;
    background: linear-gradient(90deg, #d8d8d8, #f2f2f2 50%, #d8d8d8);
    opacity: .85;
  }
  .contact { top: 94px; font-family: "Crimson Pro", serif; font-style: italic; font-weight: 700; color: var(--chalk); }
  .contact__lead { font-size: 8px; }
  .contact__row { display: flex; align-items: center; gap: 5px; font-size: 13px; margin-top: 3px; height: 18px; }
  .contact__hours { font-size: 8.5px; line-height: 10px; margin-top: 10px; }
  .icon-dot { width: 17px; height: 17px; border-radius: 50%; background: var(--icon-blue); display: flex; align-items: center; justify-content: center; }
  .icon-square { width: 15px; height: 15px; background: var(--fb-blue); margin-left: 1px; }

  .tagline { top: 208px; font-family: "Caveat", cursive; font-size: 64px; font-weight: 500; line-height: 1; white-space: nowrap; }

  .section-title { font-family: "Kalam", cursive; font-weight: 700; color: var(--gold); line-height: 1; }
  .section-title--large { font-size: 42px; }
  .section-title--medium { font-size: 22px; letter-spacing: .5px; }

  .group-title { font-family: "Kalam", cursive; font-weight: 400; font-size: 24px; line-height: 1; white-space: nowrap; }
  .group-title--small { font-size: 22px; }
  .note { font-family: "Crimson Pro", serif; font-style: italic; font-size: 10.5px; line-height: 14px; }

  .menu-list { font-family: "Oswald", sans-serif; font-weight: 500; font-size: 11px; line-height: 16px; color: var(--gold); list-style: none; }
  .menu-list li { display: flex; white-space: nowrap; }
  .menu-list .price { margin-left: auto; }
  .text-lines { font-family: "Oswald", sans-serif; font-weight: 500; font-size: 11px; line-height: 16px; color: var(--gold); }

  .rule { height: 0; border-top: 1.5px dashed var(--dash); }
  .rule--vertical { width: 0; border-top: 0; border-left: 1.5px dashed var(--dash); }

  .dish-photo { border-radius: 2px; }

  .page-label { position: absolute; top: 918px; font-family: "Fjalla One", sans-serif; font-size: 25px; color: var(--label); width: 200px; text-align: center; }
</style>
</head>
<body>
<main class="sheet">

  <section class="page page--entree">
    <h1 class="brand-name" style="left:72px;">Korvesh</h1>
    <div class="brand-band" style="left:71px;" role="img" aria-label="Geometric star lattice band with red, blue and yellow centre dots"></div>
    <div class="contact" style="left:344px;">
      <p class="contact__lead">Always Connected with us</p>
      <p class="contact__row"><span class="icon-dot"><svg width="10" height="10" viewBox="0 0 24 24"><path fill="#fff" d="M6.6 10.8a15 15 0 0 0 6.6 6.6l2.2-2.2a1 1 0 0 1 1-.25 11.4 11.4 0 0 0 3.6.57 1 1 0 0 1 1 1V20a1 1 0 0 1-1 1A17 17 0 0 1 3 4a1 1 0 0 1 1-1h3.5a1 1 0 0 1 1 1c0 1.25.2 2.45.57 3.57a1 1 0 0 1-.25 1z"/></svg></span>95551234</p>
      <p class="contact__row"><span class="icon-square"></span>Korvesh</p>
      <p class="contact__hours">Sunday - Friday 11:30-9:30<br>Saturday from 5:30-10.00<br>412 Orchard Road, Elmwood North</p>
    </div>

    <p class="tagline" style="left:56px;">Our New Menu..</p>
    <h2 class="section-title section-title--large" style="left:56px; top:282px;">Entrée</h2>

    <h3 class="group-title" style="left:56px; top:336px;">Starters</h3>
    <ul class="menu-list" style="left:56px; top:370px; width:320px;">
      <li>6 Falafel Balls On Tahini<span class="price">$5.00</span></li>
      <li>Moroccan Beef Cigars (3 per serve)<span class="price">$10.00</span></li>
      <li>Fried Cauliflower<span class="price">$8.00</span></li>
      <li>Pan Fried Mushrooms and Onions<span class="price">$8.00</span></li>
      <li>Lamb Kibbeh &amp; Pinenuts (3 per serve)<span class="price">$7.50</span></li>
    </ul>
    <div class="rule" style="left:56px; top:465px; width:316px;"></div>

    <h3 class="group-title" style="left:56px; top:482px;">Traditional Hummus</h3>
    <p class="note" style="left:56px; top:509px;">Served with 1 Laffa and MixedPickles</p>
    <ul class="menu-list" style="left:56px; top:525px; width:320px;">
      <li>Masabacha – served with Tahini and whole Chickpeas<span class="price">$11.90</span></li>
      <li>Ful– served with warm, crushed Fava Beans<span class="price">$14.90</span></li>
      <li>Mushroom– served with Pan Fried Mushrooms<span class="price">$14.90</span></li>
      <li>Basar– served with Mince Lamb &amp; Pine nuts<span class="price">$16.50</span></li>
    </ul>
    <div class="rule" style="left:56px; top:609px; width:316px;"></div>

    <h3 class="group-title" style="left:56px; top:626px;">Salads &amp; Dips Platter</h3>
    <p class="note" style="left:56px; top:652px;">3 Choices &amp; Laffa for $15.00 or 6 choices &amp; 2 Laffa for $25.00</p>
    <ul class="menu-list" style="left:56px; top:669px;">
      <li>Hummus</li><li>Tahini</li><li>Baba Ganoush</li><li>White Cabbage</li><li>Noa's Corn Salad</li>
    </ul>
    <ul class="menu-list" style="left:164px; top:669px;">
      <li>Moroccan Carrot</li><li>Roasted Beetroot</li><li>Turkish Dip</li><li>Chatzilim (Fried Eggplant)</li>
    </ul>

    <div class="dish-photo" style="left:418px; top:300px; width:104px; height:96px; background:radial-gradient(circle, #6b4a22 0%, #a8916a 45%, #f1f1ee 70%);" role="img" aria-label="Photo of falafel balls on tahini on a white plate"></div>
    <div class="dish-photo" style="left:418px; top:415px; width:104px; height:106px; background:linear-gradient(160deg, #3a3a3a, #c98e3c 45%, #e8d6b0 75%, #cfcfcf);" role="img" aria-label="Photo of fried Moroccan beef cigars"></div>
    <div class="dish-photo" style="left:418px; top:539px; width:104px; height:105px; background:radial-gradient(circle, #c9a25a 0%, #d9c59a 40%, #9a5a32 70%, #2a1a12);" role="img" aria-label="Photo of a bowl of hummus with chickpeas and herbs"></div>
    <div class="dish-photo" style="left:418px; top:662px; width:104px; height:107px; background:radial-gradient(circle, #e6d5b5 0%, #c8a97a 50%, #6f7a80 72%, #222);" role="img" aria-label="Photo of fresh baked laffa bread on a tray"></div>
  </section>

  <section class="page page--mains">
    <h1 class="brand-name" style="left:80px;">Korvesh</h1>
    <div class="brand-band" style="left:73px;" role="img" aria-label="Geometric star lattice band with red, blue and yellow centre dots"></div>
    <div class="contact" style="left:345px;">
      <p class="contact__lead">Always Connected with us</p>
      <p class="contact__row"><span class="icon-dot"><svg width="10" height="10" viewBox="0 0 24 24"><path fill="#fff" d="M6.6 10.8a15 15 0 0 0 6.6 6.6l2.2-2.2a1 1 0 0 1 1-.25 11.4 11.4 0 0 0 3.6.57 1 1 0 0 1 1 1V20a1 1 0 0 1-1 1A17 17 0 0 1 3 4a1 1 0 0 1 1-1h3.5a1 1 0 0 1 1 1c0 1.25.2 2.45.57 3.57a1 1 0 0 1-.25 1z"/></svg></span>95551234</p>
      <p class="contact__row"><span class="icon-square"></span>Korvesh</p>
      <p class="contact__hours">Sunday - Friday 11:30-9:30<br>Saturday from 5:30-10.00<br>412 Orchard Road, Elmwood North</p>
    </div>

    <p class="tagline" style="left:52px;">Our New Menu..</p>
    <h2 class="section-title section-title--medium" style="left:52px; top:277px;">Mains From the Charcoal Grill</h2>

    <h3 class="group-title" style="left:52px; top:312px;">Plates</h3>
    <p class="note" style="left:54px; top:339px;">All plates served with Hummus &amp; Tahini, Chips, Israeli salad and<br>1 Large Shashlik of your choice (Serves one person)</p>
    <ul class="menu-list" style="left:52px; top:373px; width:160px;">
      <li>Falafel Plate<span class="price">$23.00</span></li>
      <li>Chicken Liver<span class="price">$24.00</span></li>
      <li>Chicken Schnitzel Plate<span class="price">$24.00</span></li>
    </ul>
    <ul class="menu-list" style="left:255px; top:373px; width:130px;">
      <li>Kofta Shashlik<span class="price">$24.00</span></li>
      <li>Chicken Shashlik<span class="price">$24.00</span></li>
      <li>Lamb Shashlik<span class="price">$26.00</span></li>
    </ul>
    <div class="rule" style="left:52px; top:427px; width:340px;"></div>

    <h3 class="group-title" style="left:52px; top:436px;">Individual Shashilk</h3>
    <p class="note" style="left:54px; top:461px;">(1 Per serve)</p>
    <ul class="menu-list" style="left:52px; top:475px; width:160px;">
      <li>Chicken Shashlik<span class="price">$10</span></li>
      <li>Lamb Shashlik<span class="price">$11.50</span></li>
      <li>Kebab (Kofta) Shashlik<span class="price">$10.00</span></li>
    </ul>
    <ul class="menu-list" style="left:256px; top:471px; width:130px;">
      <li>Chicken Liver<span class="price">$9.50</span></li>
      <li>Schnitzel<span class="price">$11.00</span></li>
    </ul>
    <div class="rule" style="left:52px; top:530px; width:340px;"></div>

    <h3 class="group-title" style="left:52px; top:541px;">Kids Meal</h3>
    <p class="note" style="left:54px; top:567px;">(10 and under only)</p>
    <ul class="menu-list" style="left:52px; top:583px; width:160px;">
      <li>Schnitzel plate with chips</li>
      <li>and Israeli Salad<span class="price">$10.00</span></li>
      <li>Falafel Plate with chips</li>
      <li>and Israeli Salad<span class="price">$9.00</span></li>
    </ul>
    <div class="rule rule--vertical" style="left:230px; top:542px; height:106px;"></div>

    <h3 class="group-title" style="left:253px; top:541px;">Sides</h3>
    <ul class="menu-list" style="left:253px; top:567px; width:130px;">
      <li>Israeli Salad<span class="price">$10.00</span></li>
      <li>Chips<span class="price">$8.00</span></li>
      <li>Laffa<span class="price">$2.50</span></li>
      <li>Mix Pickles<span class="price">$6.00</span></li>
    </ul>
    <div class="rule" style="left:52px; top:655px; width:340px;"></div>

    <h3 class="group-title group-title--small" style="left:52px; top:660px;">$35 Set Menu</h3>
    <p class="note" style="left:58px; top:684px;">Per Person (Min 6 Person)</p>
    <p class="text-lines" style="left:52px; top:698px;">Entrée – Salads, Dips, Laffa bread&amp; Falafel<br>Main – 1 Shashlik of per Person<br>(Chicken, Kofta, lamb, Liver, Schnitzel), Chips &amp; Israeli salad<br>Dessert – Chef 's Selection</p>

    <div class="dish-photo" style="left:410px; top:300px; width:110px; height:114px; background:linear-gradient(150deg, #7a5a3a, #5a2e1a 40%, #d07a2a 65%, #eeeeea);" role="img" aria-label="Photo of a grilled shashlik plate with chips"></div>
    <div class="dish-photo" style="left:410px; top:420px; width:110px; height:107px; background:linear-gradient(180deg, #e8e8e6, #6a3820 35%, #8a4a2a 60%, #b89a6a 85%, #e8e8e6);" role="img" aria-label="Photo of grilled meat skewers on a plate"></div>
    <div class="dish-photo" style="left:410px; top:539px; width:110px; height:106px; background:radial-gradient(circle at 55% 50%, #c98a3a 0%, #b0502a 45%, #8a2a1a 70%, #1a1a1a);" role="img" aria-label="Photo of schnitzel with chips and salad"></div>
    <div class="dish-photo" style="left:410px; top:656px; width:110px; height:107px; background:linear-gradient(160deg, #2a2a2a, #9a8a4a 35%, #d8d2b8 60%, #6a5a3a);" role="img" aria-label="Photo of a spread of salads and dips"></div>
  </section>

  <p class="page-label" style="left:214px;">Page 1</p>
  <p class="page-label" style="left:830px;">Page 2</p>
</main>
</body>
</html>
```